Tour agency for FIT and groups need a business card design

We need a business card design for a tour agency company that is based in Perth called" BRISK NO", we aim to provide customise, unique and seamless travel arrangement for FIT and groups. We serve both high profile businessperson, government authorities, business partners, executives and investors. The name card should be more professional looking.
Updates

Project Deadline Extended Reason: Have some changes that needed to make, director will be back to office on Monday, sorry for the inconvenience cause. Added Saturday, May 6, 2017

Target Market(s)

High profile businessperson, government authorities, business partners, executives and investors.

Industry/Entity Type

Tourism

Contact Information for Business Card

Brisk NO
Level 1, 214 Marlowe Avenue, Dunreath NO, 6120
www.briskno.com.au

Font styles to use
Serif

Colors

Designer to choose colors to be used in the design.

Requirements
Must have
• My project must have a company logo
Nice to have
• a more professional and solid yet friendly name card design. We may want to include chinese name in the name card as well. Edge of the card can be filled with gold and we think that transparent name cards are interesting.

```html
<!DOCTYPE html>
<html lang="en">
<head>
<meta charset="utf-8">
<title>Brisk NO — Business Card</title>
<link rel="stylesheet" href="https://fonts.googleapis.com/css2?family=Crimson+Text:wght@400;600&display=swap">
<style>
  :root {
    --page: #e6e6e7;
    --charcoal: #4a4a4c;
    --sky: #1eaee3;
    --paper: #f1f1f1;
    --white: #ffffff;
    --tile: #bfbfc1;
    --ink-light: #f4f4f4;
  }
  html, body {
    margin: 0;
    width: 1027px;
    height: 1200px;
    overflow: hidden;
    background: var(--page);
  }
  .board {
    position: relative;
    width: 1027px;
    height: 1200px;
  }
  .card {
    position: absolute;
    left: 191px;
    width: 645px;
    height: 368px;
    display: block;
    font-family: "Crimson Text", serif;
  }
  .card--front { top: 163px; }
  .card--back { top: 669px; }
  .card-name { font-size: 29px; fill: var(--ink-light); }
  .card-role { font-size: 17px; fill: var(--ink-light); }
  .card-detail { font-size: 16.5px; fill: var(--ink-light); }
  .brand-name { fill: var(--sky); font-weight: 600; }
</style>
</head>
<body>
<main class="board">

  <svg class="card card--front" viewBox="0 0 806 460" role="group" aria-label="Business card front">
    <rect class="card-paper" width="806" height="460" fill="var(--paper)"/>
    <polygon class="card-panel" points="0,0 401,0 453,131 406,274 336,460 0,460" fill="var(--charcoal)"/>
    <polygon class="accent-top" points="401,0 501,0 453,131" fill="var(--sky)"/>
    <polygon class="accent-bottom" points="406,274 471,460 336,460" fill="var(--sky)"/>

    <g class="person-block">
      <rect x="0" y="86" width="74" height="56" fill="var(--sky)"/>
      <circle cx="37" cy="105" r="8" fill="#fff"/>
      <path d="M22 128 q0 -12 15 -12 q15 0 15 12 z" fill="#fff"/>
      <text class="card-name" x="94" y="109">Loream Ipsum</text>
      <text class="card-role" x="94" y="138">Travel Consultation</text>
    </g>

    <g class="contact-phone">
      <rect x="0" y="212" width="74" height="56" fill="var(--tile)"/>
      <path d="M29 230 l5 -2 l4 7 l-3 3 q3 6 8 8 l3 -3 l7 4 l-2 5 q-14 2 -22 -22 z" fill="#fff"/>
      <text class="card-detail" x="94" y="244">+61 (0)431 207 586</text>
      <text class="card-detail" x="94" y="268">08 6142 7730</text>
    </g>

    <g class="contact-web">
      <rect x="0" y="282" width="74" height="56" fill="var(--tile)"/>
      <g fill="none" stroke="#fff" stroke-width="1.6">
        <circle cx="37" cy="310" r="13"/>
        <ellipse cx="37" cy="310" rx="6" ry="13"/>
        <line x1="24" y1="310" x2="50" y2="310"/>
        <line x1="26" y1="303" x2="48" y2="303"/>
        <line x1="26" y1="317" x2="48" y2="317"/>
      </g>
      <text class="card-detail" x="94" y="307">email@briskno.com</text>
      <text class="card-detail" x="94" y="327">www.briskno.com.au</text>
    </g>

    <g class="contact-address">
      <rect x="0" y="352" width="74" height="56" fill="var(--tile)"/>
      <path d="M37 395 q-11 -13 -11 -20 a11 11 0 0 1 22 0 q0 7 -11 20 z" fill="#fff"/>
      <circle cx="37" cy="375" r="4" fill="var(--tile)"/>
      <text class="card-detail" x="94" y="374">Level 1, 214 Marlowe Avenue,</text>
      <text class="card-detail" x="94" y="398">Dunreath NO, 6120</text>
    </g>

    <text class="brand-name" x="615" y="282" font-size="50" text-anchor="middle">Brisk NO</text>
  </svg>

  <svg class="card card--back" viewBox="0 0 806 460" role="group" aria-label="Business card back">
    <rect class="card-paper" width="806" height="460" fill="var(--white)"/>
    <rect class="card-frame" x="51" y="51" width="704" height="358" fill="none" stroke="var(--sky)" stroke-width="2.5"/>
    <text class="brand-name" x="403" y="258" font-size="78" text-anchor="middle">Brisk NO</text>
  </svg>

</main>
</body>
</html>
```